BRIM Outreach Partners Business Card Rebrand

Hello Designers! We are looking for help designing our new business card to go in conjunction with our company rebrand. Unfortunately, we have an event mid June that requires we get these printed ASAP (before our new website is launched.) We have a mostly complete Brand Book which I have uploaded to this request for your reference to company information, style, fonts. I've also enclosed our logo file in .eps & .jpg. Attached is a sample business card my boss liked but said was "too simple." I made it in Canva and do not profess to be a designer. NOT FOR DESIGN REFERENCE, ONLY FOR CONTEXT Here is what our old website looks like: https://brimoutreachpartners.com/.

```html
<!DOCTYPE html>
<html lang="en">
<head>
<meta charset="utf-8">
<title>BRIM Outreach Partners – Business Card</title>
<link rel="stylesheet" href="https://fonts.googleapis.com/css2?family=Montserrat:wght@400;500;700;800&display=swap">
<style>
  :root {
    --sky: #4bb2e6;
    --ink: #111111;
    --paper: #f3f3f3;
    --stage: #e4e4e4;
  }
  * { box-sizing: border-box; margin: 0; padding: 0; }
  html, body { width: 1200px; height: 802px; overflow: hidden; }
  body {
    background: var(--stage);
    font-family: "Montserrat", sans-serif;
    display: flex;
    align-items: center;
    justify-content: center;
    gap: 40px;
  }
  .card {
    position: relative;
    width: 540px;
    height: 309px;
    overflow: hidden;
    box-shadow: 0 6px 18px rgba(0,0,0,.18);
  }

  /* Front */
  .card--front { background: var(--paper); }
  .front-shapes { position: absolute; inset: 0; }
  .front-info {
    position: absolute;
    left: 268px;
    top: 34px;
    right: 20px;
    color: var(--ink);
  }
  .wordmark {
    font-weight: 800;
    font-size: 22px;
    line-height: 1.05;
    letter-spacing: -.3px;
  }
  .person-name {
    margin-top: 26px;
    font-weight: 700;
    font-size: 15px;
    letter-spacing: .6px;
    text-transform: uppercase;
  }
  .person-role { font-size: 12px; font-weight: 400; margin-top: 2px; }
  .contact-list { list-style: none; margin-top: 18px; font-size: 10.5px; }
  .contact-list li { display: flex; align-items: center; gap: 7px; margin-bottom: 5px; white-space: nowrap; }
  .contact-list svg { width: 11px; height: 11px; flex: none; }
  .location { margin-top: 4px; font-size: 10.5px; }

  /* Back */
  .card--back { background: var(--sky); }
  .lockup {
    position: absolute;
    right: 28px;
    bottom: 56px;
    display: flex;
    align-items: center;
    gap: 14px;
  }
  .lockup-dot {
    width: 78px; height: 78px;
    border-radius: 50%;
    background: #ffffff;
  }
  .lockup-name {
    font-weight: 800;
    font-size: 26px;
    line-height: 1.05;
    color: var(--ink);
    letter-spacing: -.3px;
  }
</style>
</head>
<body>

  <section class="card card--front" aria-label="Business card front">
    <svg class="front-shapes" viewBox="0 0 540 309" width="540" height="309" aria-hidden="true">
      <polygon points="150,309 540,309 540,250" fill="var(--sky)"/>
      <circle cx="118" cy="262" r="150" fill="var(--sky)"/>
    </svg>

    <div class="front-info">
      <div class="wordmark">BRIM<br>Outreach Partners</div>
      <h1 class="person-name">Daniel Merrow-Kline</h1>
      <p class="person-role">Managing Partner</p>
      <ul class="contact-list">
        <li>
          <svg viewBox="0 0 24 24"><path fill="currentColor" d="M6.6 10.8a15 15 0 0 0 6.6 6.6l2.2-2.2c.3-.3.7-.4 1-.2 1.1.4 2.3.6 3.6.6.6 0 1 .4 1 1V20c0 .6-.4 1-1 1A17 17 0 0 1 3 4c0-.6.4-1 1-1h3.5c.6 0 1 .4 1 1 0 1.3.2 2.5.6 3.6.1.3 0 .7-.2 1z"/></svg>
          +945-555-0142
        </li>
        <li>
          <svg viewBox="0 0 24 24"><rect x="2" y="5" width="20" height="14" fill="currentColor"/><path d="M2 5l10 8 10-8" fill="none" stroke="#f3f3f3" stroke-width="2"/></svg>
          daniel@brimoutreachpartners.com
        </li>
        <li>
          <svg viewBox="0 0 24 24" fill="none" stroke="currentColor" stroke-width="2"><circle cx="12" cy="12" r="10"/><path d="M2 12h20M12 2c3 3 3 17 0 20M12 2c-3 3-3 17 0 20"/></svg>
          www.brimoutreachpartners.com
        </li>
      </ul>
      <p class="location">Columbus, OH based (Eastern Time)</p>
    </div>
  </section>

  <section class="card card--back" aria-label="Business card back">
    <div class="lockup">
      <span class="lockup-dot" aria-hidden="true"></span>
      <span class="lockup-name">BRIM<br>Outreach Partners</span>
    </div>
  </section>

</body>
</html>
```